Scientific Conference A0 Poster

I need an A0 poster for a Emergency Medicine scientific conference designed urgently. Attached is the information needed/specification,
as well as a previous poster. Your creativity is much appreciated. Here is a link to how to create a poster (no doubt things you already know), there are also examples of other posters medical posters. I want mine to be the best.
https://www.vantelquill.co.uk/briefs/how-to-make-a-poster/
Please keep the Holbury and Fenwick Care Trust and HCS logos/graphics
Please can you find a way to graphically represent the visual elements listed in the specification as well as the statistics listed in the specification. The statistics should not just be quoted, they need to be graphically represented, if possible. I am comfortable with whatever you think works.
Target Market(s)
Doctors and Healthcare management
Industry/Entity Type
Healthcare
Look and feel

```html
<!DOCTYPE html>
<html lang="en">
<head>
<meta charset="utf-8">
<title>Crowding in Emergency Departments During COVID-19</title>
<link href="https://fonts.googleapis.com/css2?family=Arimo:ital,wght@0,400;0,700;1,400&family=Bebas+Neue&family=Roboto+Condensed:ital,wght@0,400;0,700;1,400&display=swap" rel="stylesheet">
<style>
:root{
  --blue:#0b6fbf;
  --ink:#2b2b2b;
  --muted:#555;
  --panel:#f2f2f2;
  --white:#fff;
  --accent:#d9722c;
}
*{margin:0;padding:0;box-sizing:border-box}
html,body{width:1200px;height:849px;overflow:hidden;background:var(--white)}
body{position:relative;font-family:Arimo,Arial,sans-serif;color:var(--ink)}
.abs{position:absolute}
.nowrap{white-space:nowrap}

/* header */
.header-band{position:absolute;left:0;top:0;width:1200px;height:150px}
.title{left:35px;top:30px;color:var(--white);font-weight:700;font-size:43px;line-height:51px;letter-spacing:-1px}
.subtitle{left:665px;top:36px;color:var(--white);font:italic 17px/19px "Roboto Condensed",sans-serif}
.author{left:665px;top:102px;color:var(--white);font:700 14.5px/17px "Roboto Condensed",sans-serif}
.brand{right:34px;top:34px;text-align:right}
.brand-mark{display:block;color:var(--blue);font:700 38px/40px Arimo,sans-serif}
.brand-name{color:var(--ink);font:700 13px/16px Arimo,sans-serif;margin-top:6px}

/* panels */
.panel{position:absolute;background:var(--panel)}
.p1{left:0;top:152px;width:497px;height:304px}
.p2{left:499px;top:152px;width:396px;height:304px}
.p3{left:897px;top:152px;width:303px;height:403px;z-index:2;box-shadow:0 2px 0 var(--white),-2px 0 0 var(--white)}
.p4{left:0;top:459px;width:350px;height:366px}
.p5{left:352px;top:459px;width:848px;height:366px}
.footer-band{left:0;top:825px;width:1200px;height:24px;background:var(--blue)}

.sec-num{position:absolute;width:31px;height:28px;background:var(--blue);color:var(--white);font:700 24px/28px "Roboto Condensed",sans-serif;text-align:center}
.sec-title{position:absolute;font:700 23px/27px "Roboto Condensed",sans-serif;color:var(--ink);white-space:nowrap}
.rule{position:absolute;border-top:1px dashed #777;height:0}

.bullet{position:absolute;font-size:9.6px;line-height:12.8px;color:var(--ink);padding-left:18px}
.bullet::before{content:"";position:absolute;left:1px;top:2px;width:9px;height:9px;border-radius:50%;background:var(--blue);box-shadow:0 0 0 1.5px var(--panel),0 0 0 2.5px var(--blue)}

.stat{position:absolute;font-family:"Bebas Neue","Arial Narrow",sans-serif;font-weight:400;white-space:nowrap}
.stat-blue{color:var(--blue)}
.cite{position:absolute;font:italic 6px/7px Arimo,sans-serif;color:var(--ink);white-space:nowrap}

.chart-title{font:700 8px/9px Arimo,sans-serif;color:var(--ink)}
.chart-note{font:4px/5px Arimo,sans-serif;color:var(--muted)}

/* flow tree */
.pill{position:absolute;background:var(--blue);color:var(--white);font:700 9px/11px "Roboto Condensed",sans-serif;text-align:center;border-radius:3px;padding:6px 4px}
.pill small{display:block;font-weight:400;font-size:7px;line-height:8px}
.node{position:absolute;border:1.3px solid #333;border-radius:4px;background:var(--white);font:700 7px/8.5px "Roboto Condensed",sans-serif;text-align:center;display:flex;align-items:center;justify-content:center;color:var(--ink)}

/* tech */
.tech-title{position:absolute;font:700 13px/15px Arimo,sans-serif;color:var(--ink)}
.tech-body{position:absolute;font:9.6px/13px Arimo,sans-serif;color:var(--ink)}
.icon-area{position:absolute;border-radius:50%;background:var(--blue)}

/* recommendations */
.rec-title{position:absolute;font:700 15px/17px "Roboto Condensed",sans-serif;color:var(--ink)}
.rec-body{position:absolute;font:9.6px/13.5px Arimo,sans-serif;color:var(--ink)}
.refs{position:absolute;font:4.6px/5.6px Arimo,sans-serif;color:var(--ink)}
.refs p{margin-bottom:4px}
</style>
</head>
<body>

<!-- header -->
<svg class="header-band" viewBox="0 0 1200 150" aria-hidden="true">
  <polygon points="0,0 945,0 1023,150 0,150" fill="var(--blue)"/>
</svg>
<h1 class="abs title">Crowding in Emergency<br>Departments During COVID-19</h1>
<p class="abs subtitle">A Systematic Review of<br>management strategies adopted by<br>global health institutions</p>
<p class="abs author">Dr Amara Feld, Emergency Medicine Consultant</p>
<div class="abs brand">
  <span class="brand-mark">HCS</span>
  <div class="brand-name">Holbury and Fenwick<br>Care Trust</div>
</div>

<!-- 1 Introduction -->
<section class="panel p1">
  <div class="sec-num" style="left:36px;top:11px">1</div>
  <h2 class="sec-title" style="left:75px;top:13px">Introduction</h2>
  <div class="rule" style="left:36px;top:39px;width:442px"></div>

  <p class="bullet" style="left:59px;top:67px;width:172px">Emergency departments (ED) experienced unprecedented crowding during the COVID-19 pandemic.</p>
  <p class="bullet" style="left:59px;top:135px;width:172px">Hospitals faced increased healthcare demand, leading to overflows in intensive care units and emergency care, with limited hospital bed availability.</p>
  <p class="bullet" style="left:59px;top:215px;width:172px">This systematic review followed the PRISMA guidelines. Electronic databases were searched from January 2020 and December 2023.</p>

  <div class="abs" style="left:251px;top:60px;width:232px">
    <div class="chart-title" style="font-family:Georgia,serif">UK: Daily new hospital admissions for COVID-19</div>
    <div class="chart-note" style="width:200px;margin-top:2px">Hospital data is available for individual UK nations, and English data by region. Figures are not comparable between nations as reporting definitions differ across the four health systems.</div>
    <svg width="217" height="130" viewBox="0 0 232 160" preserveAspectRatio="none" style="margin-top:2px;display:block" role="img" aria-label="Line chart of daily COVID-19 hospital admissions in England from 2020 to 2023">
      <g font-family="Arimo" font-size="5" fill="#666">
        <text x="0" y="12">3,500</text><text x="0" y="32">3,000</text><text x="0" y="52">2,500</text>
        <text x="0" y="72">2,000</text><text x="0" y="92">1,500</text><text x="0" y="112">1,000</text>
        <text x="4" y="132">500</text><text x="10" y="152">0</text>
      </g>
      <line x1="18" y1="30" x2="226" y2="30" stroke="#999" stroke-dasharray="1.5 1.5" stroke-width=".6"/>
      <line x1="18" y1="110" x2="226" y2="110" stroke="#999" stroke-dasharray="1.5 1.5" stroke-width=".6"/>
      <line x1="18" y1="150" x2="226" y2="150" stroke="#999" stroke-width=".6"/>
      <polyline fill="none" stroke="var(--accent)" stroke-width="1.1" points="20,140 22,46 26,60 32,120 40,142 55,144 60,110 62,90 65,102 68,60 72,2 76,60 82,120 88,142 95,146 100,130 105,118 110,114 115,116 120,118 125,106 130,110 135,66 140,110 145,86 150,70 155,110 160,78 166,118 172,102 178,98 185,126 192,114 198,138 205,142 212,130 218,134 224,142"/>
      <text x="212" y="144" font-family="Arimo" font-size="4.5" fill="var(--accent)">England</text>
      <g font-family="Arimo" font-size="4.5" fill="#666">
        <text x="20" y="158">Mar 25, 2020</text><text x="60" y="158">Feb 24, 2021</text>
        <text x="96" y="158">Sep 12, 2021</text><text x="132" y="158">Mar 31, 2022</text>
        <text x="164" y="158">Oct 17, 2022</text><text x="204" y="158">Dec 8, 2023</text>
      </g>
    </svg>
    <div class="chart-note" style="display:flex;justify-content:space-between;width:217px;margin-top:3px"><span>Data source: Civic Health Registry (2024)</span><span>Open Health Tables | CC BY</span></div>
  </div>

  <div class="stat stat-blue" style="left:245px;top:238px;font-size:66px;line-height:52px;letter-spacing:-2px">157</div>
  <div class="stat" style="left:310px;top:237px;width:80px;text-align:right;color:var(--ink)">
    <div style="font-size:25px;line-height:22px">AVERAGE</div>
    <div style="font-size:14px;line-height:14px;letter-spacing:-.3px">DAILY ADMISSIONS</div>
    <div style="font-size:14px;line-height:14px;letter-spacing:-.3px">DURING COVID-19</div>
  </div>
  <div class="abs" style="left:399px;top:238px;width:1px;height:50px;background:#bbb"></div>
  <div class="stat" style="left:410px;top:239px;color:var(--ink)">
    <div style="font-size:18px;line-height:16px">ED SPENING</div>
    <div style="font-size:26px;line-height:22px">152 DAYS</div>
    <div style="font-size:13px;line-height:12px;letter-spacing:-.2px">IN OVERCROWDING</div>
  </div>
  <div class="cite" style="left:250px;top:292px">(Marlowe et al., 2021)</div>
</section>

<!-- 2 Impact -->
<section class="panel p2">
  <div class="sec-num" style="left:7px;top:13px">2</div>
  <h2 class="sec-title" style="left:53px;top:13px">The Impact of ED Crowding<br>During COVID-19</h2>
  <div class="rule" style="left:7px;top:40px;width:378px"></div>

  <p class="bullet" style="left:20px;top:83px;width:166px">Overcrowding peaked during the pandemic, with a 28% increase following the removal of COVID-19 lockdowns.</p>
  <p class="bullet" style="left:20px;top:146px;width:166px">This led to high-risk environments for both patients and staff, resulting in medical errors, prolonged hospital stays, and increased in-hospital mortality.</p>

  <div class="abs" style="left:197px;top:86px;width:185px">
    <div class="chart-title" style="font-size:7.5px">England and wales, number of deaths*<br><span style="font-weight:400">compared with 2016-19 average</span></div>
    <svg width="185" height="114" viewBox="0 0 185 114" style="display:block" role="img" aria-label="Line chart of weekly excess deaths in England and Wales from 2016 to 2022, with a sharp spike in 2020">
      <g font-family="Arimo" font-size="5.5" font-weight="700" fill="#333" text-anchor="end">
        <text x="178" y="14">10,000</text><text x="178" y="26">8,000</text><text x="178" y="38">6,000</text>
        <text x="178" y="50">4,000</text><text x="178" y="62">2,000</text><text x="178" y="74">0</text><text x="178" y="86">-2,000</text>
      </g>
      <polyline fill="none" stroke="#222" stroke-width=".9" points="3,76 6,70 9,74 12,68 15,73 18,70 22,75 25,69 28,72 32,67 35,74 38,70 41,66 44,73 48,71 52,74 56,72 60,76 64,70 68,73 72,72 76,74 80,70 84,73 88,72 92,60 93,24 95,58 97,62 99,70 101,73 104,74 107,71 110,72 114,40 116,58 119,76 123,70 127,73 131,66 135,72 139,68 142,70 146,64 150,68 152,64"/>
      <g font-family="Arimo" font-size="5.5" font-weight="700" fill="#333">
        <text x="6" y="100">2016</text><text x="26" y="100">17</text><text x="46" y="100">18</text>
        <text x="66" y="100">19</text><text x="86" y="100">20</text><text x="106" y="100">21</text><text x="126" y="100">22</text>
      </g>
      <text x="3" y="112" font-family="Arimo" font-size="4.5" font-weight="700" fill="#333">Sources: NSB; The Ledger Weekly</text>
      <text x="178" y="112" font-family="Arimo" font-size="4.5" fill="#333" text-anchor="end">*Four-week moving average</text>
    </svg>
  </div>

  <svg class="abs" style="left:25px;top:235px" width="58" height="56" viewBox="0 0 58 56" aria-hidden="true">
    <path d="M5 4 H53 L29 52 Z" fill="none" stroke="#222" stroke-width="5" stroke-linejoin="round"/>
    <rect x="26.5" y="12" width="5" height="20" rx="1" fill="#222"/>
    <circle cx="29" cy="39" r="3" fill="#222"/>
  </svg>
  <div class="stat stat-blue" style="left:96px;top:233px;font-size:62px;line-height:52px;letter-spacing:-1px">25%</div>
  <div class="stat" style="left:195px;top:234px;color:var(--ink)">
    <div style="font-size:36px;line-height:30px;transform:scaleX(.92);transform-origin:left center">URGENT HOSPITAL</div>
    <div style="font-size:19px;line-height:18px;transform:scaleX(.86);transform-origin:left center">ADMISSIONS DURING THE PANDEMIC</div>
  </div>
  <div class="cite" style="right:20px;top:292px">(Pennick et al., 2020)</div>
</section>

<!-- 3 Addressing -->
<section class="panel p3">
  <div class="sec-num" style="left:10px;top:13px">3</div>
  <h2 class="sec-title" style="left:58px;top:13px">Addressing ED<br>Crowding</h2>
  <div class="rule" style="left:10px;top:40px;width:270px"></div>

  <svg class="abs" style="left:0;top:0" width="303" height="403" aria-hidden="true">
    <g fill="none" stroke="#333" stroke-width="1" stroke-dasharray="2 2">
      <path d="M139 105 V124 M90 124 H188 M90 124 V137 M188 124 V137"/>
      <path d="M139 205 V222 M75 222 H206 M75 222 V235 M138 222 V235 M206 222 V235"/>
      <path d="M139 308 V328 M86 328 H194 M86 328 V338 M194 328 V338"/>
    </g>
  </svg>

  <div class="pill" style="left:83px;top:82px;width:111px">Hospital Transformations</div>
  <div class="node" style="left:50px;top:137px;width:79px;height:26px">Dedicated COVID-19<br>treatment zones</div>
  <div class="node" style="left:152px;top:137px;width:78px;height:26px">Expanding<br>telehealth services</div>

  <div class="pill" style="left:88px;top:182px;width:101px;padding:3px 4px">Process Optimisation<small>to improve patient flow</small></div>
  <div class="node" style="left:51px;top:235px;width:48px;height:27px">Fast-track<br>Pathways</div>
  <div class="node" style="left:114px;top:235px;width:48px;height:27px">Improved<br>Triage</div>
  <div class="node" style="left:182px;top:235px;width:48px;height:27px">Discharge<br>Planning</div>

  <div class="pill" style="left:86px;top:286px;width:105px">Leadership &amp; Training</div>
  <div class="node" style="left:50px;top:338px;width:72px;height:48px">Enhanced<br>adaptibility through<br>evidence based<br>training programs</div>
  <div class="node" style="left:158px;top:338px;width:72px;height:48px">Efficient ED<br>management<br>during surges</div>
</section>

<!-- 4 Technology -->
<section class="panel p4">
  <div class="sec-num" style="left:37px;top:18px">4</div>
  <h2 class="sec-title" style="left:71px;top:20px">Technological Solutions<br>for Managing ED Crowding</h2>
  <div class="rule" style="left:37px;top:46px;width:296px"></div>

  <svg class="abs" style="left:84px;top:87px" width="48" height="48" viewBox="0 0 48 48" aria-hidden="true">
    <g fill="none" stroke="var(--blue)" stroke-width="2.2" stroke-linecap="round" stroke-linejoin="round">
      <circle cx="30" cy="18" r="13"/>
      <path d="M24 14 H36 L33 11 M36 22 H24 L27 25"/>
      <path d="M5 20 L10 16 L15 23 L12 27 Q15 34 21 37 L25 34 L31 39 L27 44 Q12 40 5 20 Z"/>
    </g>
  </svg>
  <div class="tech-title" style="left:153px;top:89px">Telemedicine</div>
  <div class="tech-body" style="left:153px;top:106px;width:176px">Remote delivery of healthcare services using telecommunication technologies.</div>

  <div class="tech-title" style="left:68px;top:152px">Internet Hospitals</div>
  <div class="tech-body" style="left:68px;top:169px;width:192px">Implementation of multi-centre internet hospitals to reduce physical ED visits and crowding.</div>
  <svg class="abs" style="left:283px;top:143px" width="36" height="62" viewBox="0 0 36 62" aria-hidden="true">
    <g fill="none" stroke="var(--blue)" stroke-width="2" stroke-linecap="round">
      <path d="M3 10 Q18 -2 33 10 M8 15 Q18 7 28 15 M13 20 Q18 16 23 20"/>
      <circle cx="18" cy="24" r="2"/>
      <rect x="4" y="32" width="28" height="28"/>
      <path d="M4 38 H32 M11 44 V50 M25 44 V50 M15 53 H21 M18 50 V56"/>
    </g>
  </svg>

  <div class="icon-area" role="img" aria-label="Brain icon representing artificial intelligence" style="left:81px;top:225px;width:47px;height:49px;opacity:.8"></div>
  <div class="tech-title" style="left:153px;top:220px">AI Advancements</div>
  <div class="tech-body" style="left:153px;top:236px;width:170px">AI-enabled tools like virtual waiting rooms and online symptom checkers streamlined patient management.</div>

  <div class="stat" style="left:61px;top:292px;font-size:56px;line-height:48px;color:var(--ink);letter-spacing:-1px">1 BILLION</div>
  <div class="icon-area" role="img" aria-label="Globe showing the Americas" style="left:225px;top:290px;width:55px;height:55px"></div>
  <div class="cite" style="left:65px;top:343px;font-size:8px;line-height:10px">telehealth visits globally by the end of 2021</div>
  <div class="cite" style="left:288px;top:300px;writing-mode:vertical-rl;transform:rotate(180deg);font-weight:700;font-size:5.5px">(Thorne et al., 2021)</div>
</section>

<!-- 5 Recommendations -->
<section class="panel p5">
  <div class="sec-num" style="left:25px;top:18px">5</div>
  <h2 class="sec-title" style="left:63px;top:20px">Recommendations for<br>Future Crowding Management</h2>
  <div class="rule" style="left:25px;top:45px;width:418px"></div>
  <svg class="abs" style="left:463px;top:15px" width="58" height="58" viewBox="0 0 58 58" aria-hidden="true">
    <circle cx="29" cy="29" r="26" fill="none" stroke="var(--blue)" stroke-width="4"/>
    <path d="M17 30 L26 39 L42 21" fill="none" stroke="var(--blue)" stroke-width="4.5" stroke-linecap="round" stroke-linejoin="round"/>
  </svg>
</section>

<div class="rec-title" style="left:375px;top:563px">Data-driven Real-Time<br>Bottleneck removal</div>
<div class="rec-title" style="left:627px;top:563px">Empowered Interdepartmental<br>Collaboration</div>
<div class="rec-title" style="left:921px;top:563px">Proactive<br>Community Care</div>

<svg class="abs" style="left:374px;top:605px" width="748" height="12" aria-hidden="true">
  <line x1="6" y1="6" x2="745" y2="6" stroke="#555" stroke-width="1" stroke-dasharray="2.5 2"/>
  <circle cx="6.5" cy="6" r="4.2" fill="#222"/>
  <circle cx="255" cy="6" r="4.2" fill="#222"/>
  <circle cx="551" cy="6" r="4.2" fill="#222"/>
</svg>

<div class="rec-body" style="left:375px;top:624px;width:184px">Live dashboards pinpoint resource constraints <b><i>(imaging, labs, beds)</i></b> and patient acuity for dynamic resource allocation and on-the-fly interventions.</div>
<div class="rec-body" style="left:629px;top:624px;width:230px">Interdepartmental visibility and shared ownership of patient flow. Multidisciplinary patient flow teams. Inpatient units proactively prepare for admissions, optimising bed availability.</div>
<div class="rec-body" style="left:923px;top:624px;width:196px">Leveraging telehealth and community partnerships for remote monitoring, virtual urgent care, and preventative care to reduce ED demand.</div>

<!-- 6 References -->
<div class="sec-num" style="left:377px;top:702px">6</div>
<h2 class="sec-title" style="left:415px;top:703px">References</h2>
<div class="rule" style="left:377px;top:730px;width:770px"></div>

<div class="refs" style="left:376px;top:743px;width:381px">
  <p>Arden, P., Vosk, L., &amp; Hale, D. (2020). Emergency department crowding and hospital change during COVID-19: a retrospective study of a university hospital. Journal of Acute Care Research, 28(1), 1-10.</p>
  <p>Marlowe, J., Reyne, A., &amp; Coster, F. (2021). Emergency department overcrowding during the COVID-19 outbreak: a letter to the editor. Archives of Urgent Medicine, 9(1).</p>
  <p>Tallis, R., Brennick, K., &amp; Oaken, M. (2021). International report on emergency department crowding and access block: a brief summary. Emergency Care Journal, 38(3), 245-246.</p>
  <p>Quill, J., Danner, B., &amp; Ferro, K. (2020). Factors affecting emergency department crowding. Emergency Clinics Review, 38(3), 573-587.</p>
</div>
<div class="refs" style="left:795px;top:743px;width:354px">
  <p>Thorne, M., Sadler, F., &amp; Wren, E. (2021). A descriptive analysis of the impact of COVID-19 on emergency department attendance and visit patterns.</p>
  <p>Pennick, F., Morrow, I., &amp; Ashby, R. (2020). The changing patient flow in an orthopaedic trauma centre emergency department.</p>
  <p>Vasko, E., Tallis, R., &amp; Brandt, L. (2020). Early lessons from COVID-19 that may reduce future emergency department crowding. Emergency Care Australasia, 32(6), 1077-1079.</p>
  <p>Open Health Tables. (2023). Number of COVID-19 patients newly admitted to hospitals in a given week. Accessed 1/10/24.</p>
</div>

<div class="abs footer-band"></div>
</body>
</html>
```